Reef Glow

sunglasses, sihoullette of body, maybe wearing a bikini or sunglasses. I am offering spray tanning, body wraps, tanning beds, stand up, body art, airbrush makeup.

Target Market(s)

I would say my target is all ages, But tanning is a seasonal business and more beauty and aging concept. and around prom time I get my most profitable business. so 18 to 21 through march and april. then 25 to 55 through april to june.

Industry/Entity Type

Makeup

Contact Information for Business Card

Phone number: 701-382-5147 Owner: Jan Mortby (Lisowski)

Colors

Designer to choose colors to be used in the design.

Requirements
Nice to have
• Sunglasses, silouttes of body wearing sunglasses or bikini, or picture of spray gun.

```html
<!DOCTYPE html>
<html lang="en">
<head>
<meta charset="utf-8">
<title>Jan Mortby – Business Cards</title>
<link href="https://fonts.googleapis.com/css2?family=Arimo:wght@400&display=swap" rel="stylesheet">
<style>
  :root {
    --page: #ffffff;
    --card-sky: #eef7fa;
    --card-peach: #f8c995;
    --ink: #111111;
    --figure: #1c1816;
    --name-sun: #f0d21c;
    --name-light: #ffffff;
    --shadow: rgba(0, 0, 0, 0.35);
  }
  html, body {
    margin: 0;
    padding: 0;
    width: 1200px;
    height: 900px;
    overflow: hidden;
    background: var(--page);
    font-family: "Arimo", Arial, sans-serif;
  }
  .canvas {
    position: relative;
    width: 1200px;
    height: 900px;
  }
  .card {
    position: absolute;
    left: 336px;
    width: 570px;
    height: 332px;
    box-shadow: 3px 5px 8px var(--shadow);
  }
  .card--sky { top: 83px; background: var(--card-sky); }
  .card--peach { top: 434px; background: var(--card-peach); }

  .figure {
    position: absolute;
    left: 119px;
    top: 67px;
    width: 70px;
    height: 180px;
    background: linear-gradient(180deg, var(--figure) 0%, #3a2f2a 100%);
    border-radius: 30px 30px 6px 6px;
  }
  .card--peach .figure {
    top: 73px;
  }

  .name {
    position: absolute;
    right: 82px;
    top: 126px;
    margin: 0;
    font-size: 40px;
    font-weight: 400;
    line-height: 1;
    letter-spacing: 0.5px;
  }
  .card--sky .name { color: var(--name-sun); }
  .card--peach .name { color: var(--name-light); }

  .phone {
    position: absolute;
    right: 82px;
    top: 177px;
    margin: 0;
    font-size: 12.5px;
    color: var(--ink);
  }
  .services {
    position: absolute;
    right: 82px;
    top: 210px;
    margin: 0;
    padding: 0;
    list-style: none;
    text-align: right;
    font-size: 12.5px;
    line-height: 17.6px;
    color: var(--ink);
  }
</style>
</head>
<body>
<main class="canvas">
  <section class="card card--sky">
    <div class="figure" role="img" aria-label="Silhouette of a woman in sunglasses and a bikini"></div>
    <h1 class="name">Jan Mortby</h1>
    <p class="phone">701-382-5147</p>
    <ul class="services">
      <li>spray tanning</li>
      <li>body wraps</li>
      <li>tanning beds</li>
      <li>stand up. body art</li>
      <li>airbrush makeup</li>
    </ul>
  </section>

  <section class="card card--peach">
    <div class="figure" role="img" aria-label="Silhouette of a woman in sunglasses and a bikini"></div>
    <h1 class="name">Jan Mortby</h1>
    <p class="phone">701-382-5147</p>
    <ul class="services">
      <li>spray tanning</li>
      <li>body wraps</li>
      <li>tanning beds</li>
      <li>stand up. body art</li>
      <li>airbrush makeup</li>
    </ul>
  </section>
</main>
</body>
</html>
```